Amber Fen Racquet Club (Tennis Country Club)

Racquet and Tennis Country Club in Florida.
This web sight is needed for a Privet Tennis club located in Deerfield Beach city in Florida, USA.
We have 10 clay tennis courts and 2 hard tennis courts, small and cozy swimming pool and a clubhouse (see attached pictures) Attached pictures are for information only because we are under a reconstruction.
Updates

Target Market(s)

Adult members, Kids members, Tennis players

Coding

Coded - Design and coding required

Number of Pages Required

3 page

Requirements
Must have
• Logo colors (see attached file)

```html
<!DOCTYPE html>
<html lang="en">
<head>
<meta charset="utf-8">
<title>Amber Fen Racquet Club</title>
<link rel="stylesheet" href="https://fonts.googleapis.com/css2?family=Cinzel:wght@400&family=Montserrat:wght@500&family=PT+Serif:wght@400&display=swap">
<style>
  :root {
    --club-green: #2f6e4f;
    --ink: #3a3a3a;
    --body-ink: #4a4a4a;
    --paper: #ffffff;
    --hero-dark: #2b2b2b;
    --hero-mid: #6e6e6e;
    --hero-light: #bdbdbd;
  }
  * { margin: 0; padding: 0; box-sizing: border-box; }
  html, body {
    width: 1076px;
    height: 1200px;
    overflow: hidden;
    background: var(--paper);
  }
  .page {
    position: relative;
    width: 1076px;
    height: 1200px;
    overflow: hidden;
    background: var(--paper);
  }
  .site-header {
    position: absolute;
    top: 0; left: 0;
    width: 1076px;
    height: 172px;
    display: flex;
    align-items: center;
    justify-content: center;
  }
  .brand {
    display: flex;
    align-items: center;
    gap: 16px;
    margin-top: -84px;
  }
  .brand-dot {
    width: 60px;
    height: 60px;
    border-radius: 50%;
    border: 5px solid var(--club-green);
  }
  .brand-name {
    font-family: "Montserrat", sans-serif;
    font-weight: 500;
    font-size: 36px;
    color: var(--ink);
    letter-spacing: 0.2px;
  }
  .search-icon {
    position: absolute;
    right: 72px;
    top: 76px;
    width: 22px;
    height: 22px;
  }
  .hero {
    position: absolute;
    top: 172px; left: 0;
    width: 1076px;
    height: 512px;
    background:
      radial-gradient(ellipse at 28% 82%, rgba(230,230,230,0.55) 0%, rgba(230,230,230,0) 30%),
      linear-gradient(180deg, var(--hero-dark) 0%, var(--hero-mid) 55%, var(--hero-light) 78%, var(--hero-mid) 100%);
    display: flex;
    align-items: center;
    justify-content: center;
  }
  .hero-title {
    font-family: "Cinzel", serif;
    font-weight: 400;
    color: var(--paper);
    font-size: 68px;
    line-height: 100px;
    text-align: center;
    letter-spacing: 1px;
    margin-top: -12px;
  }
  .section-toggle {
    position: absolute;
    left: 502px;
    width: 72px;
    height: 72px;
  }
  .section-toggle.top { top: 136px; }
  .section-toggle.bottom { top: 648px; }
  .intro {
    position: absolute;
    top: 770px; left: 0;
    width: 1076px;
  }
  .intro-heading {
    position: absolute;
    left: 154px;
    top: 0;
    width: 300px;
    font-family: "Cinzel", serif;
    font-weight: 400;
    font-size: 44px;
    line-height: 66px;
    letter-spacing: 3px;
    color: var(--club-green);
    text-transform: uppercase;
  }
  .intro-text {
    position: absolute;
    left: 475px;
    top: 0;
    width: 452px;
    font-family: "PT Serif", serif;
    font-size: 18px;
    line-height: 36px;
    letter-spacing: 0.4px;
    color: var(--body-ink);
  }
</style>
</head>
<body>
<div class="page">
  <header class="site-header">
    <div class="brand">
      <span class="brand-dot"></span>
      <span class="brand-name">Amber Fen</span>
    </div>
    <svg class="search-icon" viewBox="0 0 22 22" aria-label="Search">
      <circle cx="9" cy="9" r="6.5" fill="none" stroke="var(--club-green)" stroke-width="2"/>
      <line x1="14" y1="14" x2="20" y2="20" stroke="var(--club-green)" stroke-width="2" stroke-linecap="round"/>
    </svg>
  </header>

  <section class="hero" role="img" aria-label="Black and white photo of tennis balls resting on a clay court in front of the net">
    <h1 class="hero-title">Where Florida Plays<br>Tennis.</h1>
  </section>

  <svg class="section-toggle top" viewBox="0 0 72 72" aria-label="Expand">
    <circle cx="36" cy="36" r="35" fill="var(--paper)"/>
    <line x1="24" y1="36" x2="48" y2="36" stroke="var(--ink)" stroke-width="3"/>
    <line x1="36" y1="24" x2="36" y2="48" stroke="var(--ink)" stroke-width="3"/>
  </svg>
  <svg class="section-toggle bottom" viewBox="0 0 72 72" aria-label="Expand">
    <circle cx="36" cy="36" r="35" fill="var(--paper)"/>
    <line x1="24" y1="36" x2="48" y2="36" stroke="var(--ink)" stroke-width="3"/>
    <line x1="36" y1="24" x2="36" y2="48" stroke="var(--ink)" stroke-width="3"/>
  </svg>

  <section class="intro">
    <h2 class="intro-heading">Love<br>Tennis?<br>Join the<br>Club.</h2>
    <p class="intro-text">The Amber Fen Racquet &amp; Tennis Club has been the centre of tennis activity in Deerfield, Florida for XXX years. Amber Fen boasts twelve magnificent courts, refurbished locker rooms, a swimming pool and clubhouse. There are a vast number of year-round tennis activities that keep our members game in top form including a variety of Round Robins, evening House Leagues for men and women, numerous Interclub teams, competitive and social tournaments, plus private lessons taught by our team of seasoned professionals.</p>
  </section>
</div>
</body>
</html>
```